Online Shop Maren

We need a web design for an online shop, called "Lorvi Tenk Jewels". The shop should have an extraordinary, elegant look, as shown in the Quillane Advertising Picture in our Briefing.pdf (attached). Please have a look at our Briefing regarding website colours, background ideas, and elements to be included. The online shop is about professional jewellery design pieces, where each piece is handmade of high quality materials, also unique pieces and unique editions possible. It should attract extraordinary people and visualize that its a very individual and unique design jewellery. You can get an idea of whom it should attract by reading our target group. Colours to be used are jewellery-Velvet red, Black / anthracite, exclusive colours, silverish-white, bronze-brown and golden.

Please play around when designing with the image pictures we attach, preferably more vertical pictures, no panoramic pictures like in Dorvena Shop. Also include the BLACK logo of lorvi tenk. We include the SITEMAP in the briefing and also another folder with product pictures you can use for the draft.

Regarding Functions, the store will have the SAME (technical) functions as this page:http://www.dorvena-shop.example/ - using the "most famous" products/categories for the starting page, going into individual product pages by clicking these images and then leading to a detailed page for one product only.

Target Market(s)

Jewellery-lovers, who appreciate extraordinary things, creative economy/fashion-industries, stylists, Style consultants, outfitter, theatres, operas, production sites, Cocktail-, Dinner and Bridefashion, exclusive traditional costume stores, dancesports and tango argento dancers

Industry/Entity Type

Shop

Requirements
Must have
• Must include:
• Colours as per briefing
• Background ideas/images as per briefing/pictures sent
• Sitemap as per briefing
• Social buttons
• Logo
• Design for 3 pages: Starting page showing big images, attractive design and the 4 popular categories
• Subpage with different products of one category (i.e. bracelets)
• Detail page with one individual product only
Should not have
• no fresh, playful colours like yellow, orange, green, blue
• no cheap design, no panorama pictures

```html
<!DOCTYPE html>
<html lang="en">
<head>
<meta charset="utf-8">
<title>Lorvi Tenk Jewels – Online Shop</title>
<link href="https://fonts.googleapis.com/css2?family=Open+Sans:wght@400;600;700&family=Raleway:wght@400;500&family=Great+Vibes&family=Oswald:wght@500&display=swap" rel="stylesheet">
<style>
:root{
  --page:#060606;
  --footer:#0e0e0e;
  --line:#262626;
  --gold:#d9a441;
  --gold-soft:#e8bf6a;
  --white:#ffffff;
  --text:#8a8a8a;
  --muted:#7a7a7a;
  --button:#262626;
}
*{margin:0;padding:0;box-sizing:border-box}
html,body{width:729px;height:1200px;overflow:hidden;background:var(--page)}
body{position:relative;font-family:"Open Sans",Arial,sans-serif;color:var(--text)}
.abs{position:absolute}
a{color:inherit;text-decoration:none}

/* hero */
.hero{left:0;top:0;width:729px;height:396px;
  background:
   radial-gradient(ellipse 120px 150px at 515px 300px,rgba(236,234,238,.95) 0%,rgba(200,196,204,.7) 40%,transparent 100%),
   radial-gradient(ellipse 70px 60px at 565px 360px,rgba(220,200,205,.7) 0%,transparent 100%),
   radial-gradient(ellipse 60px 80px at 470px 150px,rgba(120,96,92,.8) 0%,transparent 100%),
   radial-gradient(ellipse 170px 240px at 500px 250px,#3a3238 0%,#26232a 55%,transparent 100%),
   linear-gradient(90deg,#050506 0%,#0a0b0e 30%,#171c26 55%,#2c3646 78%,#3a4658 90%,#232a36 100%)}
.hero-fade{left:0;top:330px;width:729px;height:66px;background:linear-gradient(180deg,transparent,rgba(6,6,6,.55))}

/* header */
.logo-name{left:86px;top:8px;font-size:20px;color:var(--white);line-height:26px}
.logo-sub{left:125px;top:36px;font-size:11px;color:var(--white)}
.search{left:446px;top:13px;width:124px;height:15px;border:1px solid #3a3a3a;background:#0a0a0a;font-size:6px;color:#9a9a9a;padding:3px 5px}
.search svg{position:absolute;right:3px;top:2px}
.account{left:580px;top:15px;font-size:7px;color:var(--white)}
.nav{top:46px;font-size:7px;color:var(--white)}
.nav-sep{top:46px;width:1px;height:9px;background:#444}
.basket{left:568px;top:46px;font-size:7px;color:var(--gold)}
.header-rule{left:86px;top:62px;width:557px;height:1px;background:rgba(255,255,255,.12)}

.hero-script{font-family:"Great Vibes",cursive;color:var(--gold);line-height:1}
.hero-tagline{left:99px;top:212px;font-family:"Raleway",sans-serif;font-size:11.5px;color:var(--white)}
.save{left:146px;top:240px;font-family:"Great Vibes",cursive;font-size:21px;color:var(--white)}
.fifty{left:139px;top:254px;font-family:"Oswald",sans-serif;font-size:60px;font-weight:500;color:var(--white);line-height:66px}
.off{left:192px;top:262px;width:20px;height:52px;background:var(--white);border-radius:10px;color:#111;font-size:8px;font-weight:700;writing-mode:vertical-rl;transform:rotate(180deg);text-align:center;line-height:20px}
.percent{left:214px;top:277px;font-size:30px;font-weight:700;color:var(--white);line-height:36px}
.shop-now{left:152px;top:336px;width:74px;height:20px}
.shop-now span{position:absolute;left:0;top:0;width:74px;text-align:center;line-height:20px;font-size:8px;font-weight:700;color:var(--white)}
.arrow{top:220px;width:22px;height:22px;background:rgba(120,120,120,.55)}

/* sidebar */
.side-title{left:85px;font-family:"Raleway",sans-serif;font-size:11px;color:var(--gold)}
.side-rule{left:85px;width:103px;height:1px;background:var(--line)}
.side-item{left:85px;font-size:7px;color:var(--muted)}
.side-item::before{content:"";display:inline-block;border-left:3px solid #555;border-top:2px solid transparent;border-bottom:2px solid transparent;margin-right:4px}

/* main */
.welcome{left:222px;top:414px;font-family:"Raleway",sans-serif;font-size:14px;font-weight:400;color:var(--gold)}
.intro{left:222px;top:438px;width:422px;font-size:7.3px;line-height:12.4px;color:#8c8c8c;hyphens:auto;text-align:left}
.main-rule{left:222px;top:513px;width:421px;height:1px;background:var(--line)}
.popular{left:222px;top:525px;font-family:"Raleway",sans-serif;font-size:11px;font-weight:400;color:var(--gold)}
.product{width:91px}
.product-image{width:91px;height:97px;border:1px solid #4a4a4a}
.tone-silver{background:radial-gradient(ellipse 40px 44px at 50% 52%,#cfcfd2 0%,#8a8a8e 40%,#3d3d40 100%)}
.tone-crystal{background:radial-gradient(ellipse 22px 30px at 50% 45%,#e6e6ea 0%,#8e8e92 45%,#353538 100%)}
.tone-pearl{background:radial-gradient(ellipse 30px 44px at 50% 55%,#f2efe8 0%,#b7b2a6 40%,#3a3935 100%)}
.tone-bracelet{background:radial-gradient(ellipse 44px 40px at 50% 50%,#ece6e2 0%,#a9a2a0 45%,#4a4646 100%)}
.tone-tassel{background:radial-gradient(ellipse 20px 38px at 50% 55%,#bdbdc0 0%,#6c6c70 45%,#2e2e31 100%)}
.tone-gold{background:radial-gradient(ellipse 40px 36px at 50% 50%,#b58a3c 0%,#6b5434 45%,#2e2b28 100%)}
.tone-ring{background:radial-gradient(ellipse 34px 30px at 50% 55%,#f4f4f6 0%,#a8a8ad 45%,#3a3a3d 100%)}
.tone-collar{background:radial-gradient(ellipse 42px 36px at 50% 45%,#dcdcde 0%,#9a9a9e 40%,#4a4a4c 100%)}
.product-name{margin-top:8px;text-align:center;font-size:7.5px;font-weight:700;color:var(--white)}
.product-line{text-align:center;font-size:7px;color:var(--muted);line-height:10px}
.product-price{margin-top:3px;text-align:center;font-size:10px;font-weight:700;color:#8d8d8d}
.product-button{margin:4px auto 0;width:55px;height:16px;background:var(--button);color:#bdbdbd;font-size:7px;text-align:center;line-height:16px}

/* footer */
.footer{left:0;top:928px;width:729px;height:272px;background:var(--footer);border-top:1px solid #1c1c1c}
.f-title{font-family:"Raleway",sans-serif;font-size:9px;color:var(--gold);line-height:11px}
.f-text{font-size:7px;color:#a0a0a0;line-height:10px}
.email-input{left:85px;top:998px;width:122px;height:16px;background:var(--white);font-size:6.5px;color:#999;padding:4px}
.submit{left:212px;top:998px;width:40px;height:16px;background:var(--gold-soft);color:#111;font-size:7.5px;font-weight:700;text-align:center;line-height:16px}
.social{font-size:7px;color:#a0a0a0}
.social i{display:inline-block;width:8px;height:8px;margin-right:5px;vertical-align:-1px}
.pay-card{top:978px;width:30px;height:18px;border:1px solid #ddd;border-radius:1px}
.f-rule{left:85px;width:557px;height:1px;background:#1f1f1f}
.links{font-size:7px;color:#a0a0a0;line-height:13.6px;list-style:none}
.contact-line{font-size:7px;color:#a0a0a0;line-height:10px}
.copyright{left:92px;top:1172px;font-size:7.5px;color:#a0a0a0}
.foot-logo{left:551px;top:1161px;font-size:15px;color:var(--white);line-height:20px}
.foot-logo-sub{left:581px;top:1183px;font-size:8px;color:var(--white)}
</style>
</head>
<body>

<div class="abs hero" role="img" aria-label="Hero photograph: woman in a white jacket wearing a silver statement necklace by a window"></div>
<div class="abs hero-fade"></div>

<header>
  <div class="abs logo-name">Lorvi Tenk</div>
  <div class="abs logo-sub">Jewels</div>
  <div class="abs search">ENTER YOUR SEARCH...
    <svg width="9" height="9" viewBox="0 0 9 9"><circle cx="3.8" cy="3.8" r="2.8" fill="none" stroke="#888" stroke-width="1"/><line x1="6" y1="6" x2="8.5" y2="8.5" stroke="#888" stroke-width="1"/></svg>
  </div>
  <div class="abs account">LOGIN &nbsp;|&nbsp; REGISTER</div>
  <nav>
    <a class="abs nav" style="left:258px">HOME</a>
    <span class="abs nav-sep" style="left:287px"></span>
    <a class="abs nav" style="left:296px">ONLINE SHOP</a>
    <span class="abs nav-sep" style="left:348px"></span>
    <a class="abs nav" style="left:358px">INFO &amp; FACTS</a>
    <span class="abs nav-sep" style="left:410px"></span>
    <a class="abs nav" style="left:420px">PARTNER</a>
    <span class="abs nav-sep" style="left:457px"></span>
    <a class="abs nav" style="left:466px">ABOUT ME</a>
    <span class="abs nav-sep" style="left:511px"></span>
    <a class="abs nav" style="left:520px">CONTACT</a>
    <span class="abs nav-sep" style="left:557px"></span>
    <a class="abs basket">
      <svg width="9" height="8" viewBox="0 0 9 8" style="vertical-align:-1px;margin-right:3px"><path d="M0 1h2l1 4h5l1-3H2.6" fill="none" stroke="#d9a441" stroke-width="1"/><circle cx="3.5" cy="7" r=".9" fill="#d9a441"/><circle cx="7" cy="7" r=".9" fill="#d9a441"/></svg>BASKET: 0 &nbsp;ITEM(s)</a>
  </nav>
  <div class="abs header-rule"></div>
</header>

<section class="hero-copy">
  <div class="abs hero-script" style="left:92px;top:106px;font-size:42px">Fine</div>
  <div class="abs hero-script" style="left:160px;top:118px;font-size:42px">Jewel</div>
  <div class="abs hero-script" style="left:102px;top:152px;font-size:64px">Edition</div>
  <div class="abs hero-tagline">Our Best Values on Our Best Items</div>
  <div class="abs save">Save upto</div>
  <div class="abs fifty">50</div>
  <div class="abs off">OFF</div>
  <div class="abs percent">%</div>
  <a class="abs shop-now">
    <svg width="74" height="20" viewBox="0 0 74 20"><path d="M1 1h72l-5 9 5 9H1l5-9z" fill="#0a0a0a" stroke="#cfcfcf" stroke-width="1"/></svg>
    <span>SHOP NOW</span>
  </a>
  <div class="abs arrow" style="left:0"><svg width="22" height="22" viewBox="0 0 22 22"><path d="M13 6l-5 5 5 5" fill="none" stroke="#fff" stroke-width="1.2"/></svg></div>
  <div class="abs arrow" style="left:707px"><svg width="22" height="22" viewBox="0 0 22 22"><path d="M9 6l5 5-5 5" fill="none" stroke="#fff" stroke-width="1.2"/></svg></div>
</section>

<aside>
  <div class="abs side-title" style="top:414px">Shop Categories</div>
  <div class="abs side-rule" style="top:430px"></div>
  <a class="abs side-item" style="top:435px">Collier</a>
  <a class="abs side-item" style="top:451px">Bracelet</a>
  <a class="abs side-item" style="top:467px">Ring</a>
  <a class="abs side-item" style="top:483px">Earring</a>
  <div class="abs side-title" style="top:509px">Online Shop</div>
  <div class="abs side-rule" style="top:525px"></div>
  <a class="abs side-item" style="top:530px">Collections</a>
  <a class="abs side-item" style="top:546px">Houte Couture</a>
  <a class="abs side-item" style="top:562px">Vouchers</a>
</aside>

<main>
  <h1 class="abs welcome">Welcome To Lorvi Tenk Jewels</h1>
  <p class="abs intro">This is Pixelshop's version &nbsp;of Lorem Ipsum. Proin gravida nibh vel velit auctor aliquet. Aenean sollicitudin, lorem quis bibendum auctor, nisi elit consequat ipsum, nec sagittis sem nibh id elit. Duis sed odio sit amet nibh vulpu&shy;tate cursus a sit amet mauris. Morbi accumsan ipsum velit. Nam nec tellus a odio tincidunt auctor a ornare odio. Sed non &nbsp;mauris vitae erat consequat auctor eu in elit. Class aptent taciti sociosqu ad litora torquent per conubia nostra, per inceptos himenaeos.</p>
  <div class="abs main-rule"></div>
  <h2 class="abs popular">Most Popular Products</h2>

  <div class="abs product" style="left:222px;top:553px"><div class="product-image tone-silver" role="img" aria-label="Silver wire crescent earrings"></div><div class="product-name">Lorem Ipsum</div><div class="product-line">Fine Jewel Edition</div><div class="product-price">€55</div><div class="product-button">SHOP NOW</div></div>
  <div class="abs product" style="left:332px;top:553px"><div class="product-image tone-crystal" role="img" aria-label="Crystal tube pendant on a wire choker"></div><div class="product-name">Lorem Ipsum</div><div class="product-line">Fine Jewel Edition</div><div class="product-price">€55</div><div class="product-button">SHOP NOW</div></div>
  <div class="abs product" style="left:442px;top:553px"><div class="product-image tone-pearl" role="img" aria-label="Pearl drop earrings with gold accents"></div><div class="product-name">Lorem Ipsum</div><div class="product-line">Fine Jewel Edition</div><div class="product-price">€55</div><div class="product-button">SHOP NOW</div></div>
  <div class="abs product" style="left:552px;top:553px"><div class="product-image tone-bracelet" role="img" aria-label="Stacked crystal bead bracelets"></div><div class="product-name">Lorem Ipsum</div><div class="product-line">Fine Jewel Edition</div><div class="product-price">€55</div><div class="product-button">SHOP NOW</div></div>

  <div class="abs product" style="left:222px;top:734px"><div class="product-image tone-tassel" role="img" aria-label="Beaded tassel pendant necklace"></div><div class="product-name">Lorem Ipsum</div><div class="product-line">Fine Jewel Edition</div><div class="product-price">€55</div><div class="product-button">SHOP NOW</div></div>
  <div class="abs product" style="left:332px;top:734px"><div class="product-image tone-gold" role="img" aria-label="Gold beaded necklace with diamond-shaped drops"></div><div class="product-name">Lorem Ipsum</div><div class="product-line">Fine Jewel Edition</div><div class="product-price">€55</div><div class="product-button">SHOP NOW</div></div>
  <div class="abs product" style="left:442px;top:734px"><div class="product-image tone-ring" role="img" aria-label="Crystal bead cluster ring"></div><div class="product-name">Lorem Ipsum</div><div class="product-line">Fine Jewel Edition</div><div class="product-price">€55</div><div class="product-button">SHOP NOW</div></div>
  <div class="abs product" style="left:552px;top:734px"><div class="product-image tone-collar" role="img" aria-label="Silver crystal lace collar necklace"></div><div class="product-name">Lorem Ipsum</div><div class="product-line">Fine Jewel Edition</div><div class="product-price">€55</div><div class="product-button">SHOP NOW</div></div>
</main>

<footer>
  <div class="abs footer"></div>

  <div class="abs f-title" style="left:85px;top:943px">Exclusive Email Offers</div>
  <p class="abs f-text" style="left:85px;top:962px;width:160px">Enter your email address below to receive occasional offers, discounts, and promotions Lorvi Tenk Jewels.</p>
  <div class="abs email-input">Enter Email Address...</div>
  <div class="abs submit">SUBMIT</div>

  <div class="abs f-title" style="left:281px;top:943px">Connect We're Social</div>
  <a class="abs social" style="left:281px;top:962px"><i style="background:#3b5a98"></i>Follow us Friendwall</a>
  <a class="abs social" style="left:281px;top:980px"><i style="background:#2a9fd8"></i>Follow us Chirpline</a>
  <a class="abs social" style="left:281px;top:997px"><i style="background:#1c6fa8"></i>Follow us Linkwork</a>
  <a class="abs social" style="left:375px;top:962px"><i style="background:#c8402f"></i>Follow us Globbe+</a>
  <a class="abs social" style="left:375px;top:980px"><i style="background:#1fa3d8"></i>Follow us Talkwave</a>
  <a class="abs social" style="left:375px;top:997px"><i style="background:#c8302a"></i>Follow us Vidstream</a>

  <div class="abs f-title" style="left:476px;top:943px;width:160px">We Accept the following Payment Methods</div>
  <div class="abs pay-card" style="left:476px;background:#f2f2f2"></div>
  <div class="abs pay-card" style="left:510px;background:#f2f2f2"></div>
  <div class="abs pay-card" style="left:544px;background:#2a7fc0"></div>
  <div class="abs pay-card" style="left:578px;background:#f2f2f2"></div>
  <div class="abs pay-card" style="left:613px;background:#1a4fa0"></div>

  <div class="abs f-rule" style="top:1032px"></div>

  <div class="abs f-title" style="left:85px;top:1047px">Quick Links</div>
  <ul class="abs links" style="left:85px;top:1061px"><li>Home</li><li>Online SHop</li><li>Info &amp; Facts</li><li>Partner</li><li>About Me</li><li>Contact</li></ul>
  <div class="abs f-title" style="left:199px;top:1047px">Online Shop</div>
  <ul class="abs links" style="left:199px;top:1061px"><li>Collections</li><li>Houte Couture</li><li>Vouchers</li></ul>
  <div class="abs f-title" style="left:314px;top:1047px">Policies</div>
  <ul class="abs links" style="left:314px;top:1061px"><li>Return Policy</li><li>Cancellation Policy</li><li>Warranty Policy</li><li>Shipping Policy</li><li>Privacy Policy</li></ul>
  <div class="abs f-title" style="left:437px;top:1047px">Help</div>
  <ul class="abs links" style="left:437px;top:1061px"><li>FAQs</li><li>Contact Us</li><li>Order Status</li><li>Return Center</li></ul>
  <div class="abs f-title" style="left:527px;top:1047px">Contact Us</div>
  <svg class="abs" style="left:533px;top:1064px" width="10" height="14" viewBox="0 0 10 14"><path d="M5 0C2.2 0 0 2.2 0 5c0 3.6 5 9 5 9s5-5.4 5-9C10 2.2 7.8 0 5 0z" fill="#9a9a9a"/><circle cx="5" cy="5" r="1.8" fill="#0e0e0e"/></svg>
  <p class="abs contact-line" style="left:551px;top:1063px">225,, Your Location, Street,<br>City, 125605</p>
  <svg class="abs" style="left:534px;top:1094px" width="8" height="13" viewBox="0 0 8 13"><rect x=".5" y=".5" width="7" height="12" rx="1.2" fill="none" stroke="#9a9a9a"/><line x1="3" y1="10.5" x2="5" y2="10.5" stroke="#9a9a9a"/></svg>
  <p class="abs contact-line" style="left:551px;top:1096px">+1 (888) XXX XXXX</p>

  <div class="abs f-rule" style="top:1155px"></div>
  <p class="abs copyright">© 2013 Lorvi Tenk Jewels. All Rights Reserved.</p>
  <div class="abs foot-logo">Lorvi Tenk</div>
  <div class="abs foot-logo-sub">Jewels</div>
</footer>

</body>
</html>
```